vantrel works cybersecurity website design and development

website design and development for a cybersecurity company. we have a logo and would like site to suit logo colors and look
cybersecurity website should be secure and look professional
main example of site we want to use: https://www.morvisquad.example/
site should be usable on tablet and phones

For each design proposal, please could you provide details of what language you'll use to code the website.

Target Market(s)

insurance companies, financial institutions, private SME, Africa and Europe

Coding

Coded - Design and coding required

Number of Pages Required

5+ page

Requirements
Must have
• 9 Pages:
Home
About us
Contacts
Partners
Blog
Services
( consulting, vulnerability assessment, information systems security audit, ISO compliance, Penetration testing, security awareness training, social engineering test, protection against DDoS, procurement )
Resources
Technologies
Careers
Nice to have
• nice to have all services have their own pages.
design based on logo colors and look

please provide what will be use to code the website

```html
<!DOCTYPE html>
<html lang="en">
<head>
<meta charset="utf-8">
<title>Vantrel Works — Cyber Security</title>
<meta name="viewport" content="width=1200">
<link href="https://fonts.googleapis.com/css2?family=Poppins:wght@400;500;600;700;800;900&display=swap" rel="stylesheet">
<style>
:root{
  --navy:#182a7c;
  --navy-deep:#0f1d5c;
  --blue:#1f62c8;
  --blue-bright:#1d8fe0;
  --sky:#2aa0ec;
  --red:#e8392b;
  --ink:#1a1a24;
  --text:#3a3a46;
  --dark:#17171d;
  --news-bg:#e4e7f0;
  --white:#ffffff;
  --muted:#c9d6f2;
}
*{margin:0;padding:0;box-sizing:border-box}
html,body{width:1200px;height:4853px;overflow:hidden}
body{font-family:'Poppins',sans-serif;color:var(--text);background:var(--white)}
.page{position:relative;width:1200px;height:4853px;overflow:hidden}
section,header,footer,nav{position:absolute;left:0;width:1200px}
.abs{position:absolute}
.btn{position:absolute;display:flex;align-items:center;justify-content:center;background:var(--blue-bright);color:var(--white);font-weight:600;font-size:13px;letter-spacing:1.5px;border-radius:22px;text-transform:uppercase}
.section-title{position:absolute;left:0;width:1200px;text-align:center;font-weight:700;font-size:40px;color:var(--navy)}
.brand{display:flex;align-items:center;gap:10px;font-weight:600;font-size:22px;color:var(--navy)}
.brand-dot{width:40px;height:40px;border-radius:50%;background:var(--blue)}

/* header */
.site-header{top:0;height:68px;background:var(--white)}
.site-header .brand{position:absolute;left:158px;top:10px}
.get-started{position:absolute;left:917px;top:11px;width:125px;height:42px;background:var(--blue-bright);color:var(--white);font-weight:600;font-size:13px;display:flex;align-items:center;justify-content:center;border:2px solid #7cc4f2}
.main-nav{top:68px;height:49px;background:var(--navy)}
.main-nav ul{list-style:none;display:flex;position:absolute;left:158px;top:0;height:49px}
.main-nav li{color:var(--white);font-size:14px;padding:0 15px;display:flex;align-items:center}
.main-nav li.active{background:var(--blue-bright);padding:0 22px}

/* hero */
.hero{top:117px;height:520px;background:linear-gradient(120deg,#1a3a9a 0%,#1f5fbf 55%,#2a8ad5 100%)}
.hero h1{position:absolute;left:155px;top:82px;font-weight:900;font-size:92px;line-height:86px;color:var(--white);letter-spacing:1px}
.hero .slide-num{position:absolute;top:292px;font-size:19px;color:var(--white)}
.hero .slide-line{position:absolute;left:222px;top:304px;width:128px;height:2px;background:var(--sky)}
.hero .slide-title{position:absolute;left:405px;top:286px;font-size:22px;font-weight:500;color:var(--red)}
.hero p{position:absolute;left:405px;top:322px;width:280px;font-size:14px;line-height:24px;color:var(--white)}
.hero-art{position:absolute;left:672px;top:81px;width:370px;height:358px}
.dots{position:absolute;display:flex;gap:11px}
.dots span{width:9px;height:9px;border-radius:50%;background:var(--white)}
.dots span.ring{background:transparent;border:1.5px solid currentColor}

/* services */
.services{top:637px;height:535px;background:var(--white)}
.services .section-title{top:58px;color:var(--navy)}
.service-card{position:absolute;top:137px;width:285px;height:251px;background:linear-gradient(160deg,#1c6fd0 0%,#1c4fb8 60%,#1d5fc6 100%);color:var(--white);padding:22px 24px}
.service-card .head{display:flex;gap:14px;align-items:flex-start}
.service-card svg{flex:none}
.service-card h3{font-weight:600;font-size:22px;line-height:26px}
.service-card p{position:absolute;left:24px;top:140px;width:240px;font-size:13px;line-height:22px}

/* about */
.about{top:1172px;height:760px}
.about-bg{position:absolute;left:0;top:0}
.about h2{position:absolute;left:157px;top:142px;font-size:40px;font-weight:700;color:var(--white)}
.about .lead{position:absolute;left:157px;top:200px;width:460px;font-size:13px;line-height:24px;color:var(--white)}
.about-art{position:absolute;left:158px;top:311px;width:435px;height:430px}
.feature{position:absolute;left:669px;width:380px;color:var(--white)}
.feature h4{font-size:17px;font-weight:600;display:flex;align-items:center;gap:10px}
.feature p{margin-left:43px;margin-top:6px;font-size:13px;line-height:23px}

/* technologies */
.tech{top:1932px;height:785px}
.tech-bg{position:absolute;left:0;top:0}
.tech-art{position:absolute;left:269px;top:67px;width:664px;height:354px;border:4px solid var(--white);background:linear-gradient(135deg,#3a4150 0%,#1a1e28 55%,#101318 100%);box-shadow:0 6px 18px rgba(0,0,0,.35)}
.play{position:absolute;left:289px;top:134px;width:86px;height:86px;border-radius:50%;border:3px solid var(--white);background:rgba(0,0,0,.35);display:flex;align-items:center;justify-content:center}
.tech h2{position:absolute;left:273px;top:452px;font-size:42px;font-weight:700;color:var(--white)}
.tech p{position:absolute;left:275px;top:524px;width:630px;font-size:13px;line-height:23px;color:var(--white)}

/* resources */
.resources{top:2717px;height:697px;background:var(--dark)}
.resources .section-title{top:69px;color:var(--white)}
.res-item{position:absolute;width:260px;text-align:center;color:var(--white)}
.res-item h4{font-size:17px;font-weight:600}
.res-item p{font-size:13px;line-height:22px;margin-top:4px;color:#e4e4ea}
.res-art{position:absolute;left:470px;top:157px;width:260px;height:255px}

/* news */
.news{top:3414px;height:501px;background:var(--news-bg)}
.news .section-title{top:60px;color:var(--navy)}
.news-card{position:absolute;top:132px;width:285px}
.news-card .thumb{width:285px;height:186px;position:relative}
.news-card .date{position:absolute;right:12px;top:16px;width:56px;height:46px;background:var(--blue-bright);color:var(--white);font-size:13px;font-weight:600;line-height:17px;text-align:center;padding-top:6px}
.news-card h4{margin-top:14px;font-size:16px;font-weight:600;line-height:25px;color:var(--ink)}
.news-card .btn{position:static;width:121px;height:36px;margin-top:10px}

/* partners */
.partners{top:3915px;height:350px;background:var(--white)}
.partners .section-title{top:62px}
.partner{position:absolute;top:180px;display:flex;align-items:center;gap:8px;font-size:17px;font-weight:500;color:#5a5a66}
.partner i{display:block;width:22px;height:22px;border-radius:50%;background:#9aa3b8}

/* footer */
.site-footer{top:4265px;height:588px;background:linear-gradient(180deg,#0f1d5c 0%,#16297c 100%);color:var(--white)}
.site-footer .brand{position:absolute;left:158px;top:100px;color:var(--white)}
.site-footer .brand-dot{background:var(--blue-bright)}
.footer-about{position:absolute;left:157px;top:162px;width:290px;font-size:13px;line-height:24px}
.contact-line{position:absolute;left:157px;display:flex;gap:12px;font-size:13px;line-height:20px}
.footer-col{position:absolute;top:112px}
.footer-col h5{font-size:15px;font-weight:500;color:var(--sky);margin-bottom:18px;letter-spacing:.3px}
.footer-col li{list-style:none;font-size:13px;line-height:20px;margin-bottom:11px}
.copyright{position:absolute;left:157px;top:480px;font-size:12px}
.follow{position:absolute;left:830px;top:470px;display:flex;align-items:center;gap:8px;font-size:14px}
.follow span.s{width:33px;height:33px;border-radius:50%;background:var(--white)}
</style>
</head>
<body>
<div class="page">

<header class="site-header">
  <div class="brand"><span class="brand-dot"></span>Vantrel Works</div>
  <a class="get-started">Get Started</a>
</header>

<nav class="main-nav">
  <ul>
    <li class="active">Home</li><li>Services</li><li>About us</li><li>Resources</li><li>Technologies</li><li>Careers</li><li>Partners</li><li>Blog</li><li>Contacts</li>
  </ul>
</nav>

<section class="hero">
  <h1>CYBER<br>SECURITY</h1>
  <span class="slide-num" style="left:198px">01</span>
  <span class="slide-line"></span>
  <span class="slide-num" style="left:363px">04</span>
  <span class="slide-title">Lorem Ipsum</span>
  <p>Many desktop publishing packages and web page editors now use Lorem Ipsum as their .</p>
  <svg class="hero-art" viewBox="0 0 370 358" role="img" aria-label="Illustration of a glowing padlock inside a shield emblem">
    <defs><linearGradient id="heroShield" x1="0" y1="0" x2="0" y2="1"><stop offset="0" stop-color="#2a7fdc"/><stop offset="1" stop-color="#0d1a48"/></linearGradient></defs>
    <path d="M185 4 C260 4 330 20 366 40 C366 190 300 300 185 354 C70 300 4 190 4 40 C40 20 110 4 185 4Z" fill="url(#heroShield)" stroke="#ffffff" stroke-width="4"/>
  </svg>
  <div class="dots" style="left:575px;top:469px;color:#fff"><span></span><span class="ring"></span><span></span></div>
</section>

<section class="services">
  <h2 class="section-title">Our Services</h2>
  <div class="service-card" style="left:157px">
    <div class="head">
      <svg width="44" height="44" viewBox="0 0 44 44" fill="none" stroke="#fff" stroke-width="2"><circle cx="26" cy="14" r="9"/><circle cx="26" cy="14" r="3"/><path d="M4 34h10l8 4 14-6M4 30h8l8 2"/></svg>
      <h3>Consulting</h3>
    </div>
    <p>It is a long established fact that a reader will be distracted by the readable of a page .</p>
  </div>
  <div class="service-card" style="left:458px">
    <div class="head">
      <svg width="44" height="44" viewBox="0 0 44 44" fill="none" stroke="#fff" stroke-width="2"><rect x="6" y="6" width="24" height="32" rx="2"/><path d="M12 14h12M12 20h12M12 26h8"/><path d="M32 18l6 3v6c0 5-3 8-6 9-3-1-6-4-6-9v-6z"/></svg>
      <h3>Vulnerability Assessment</h3>
    </div>
    <p>It is a long established fact that a reader will be distracted by the readable of a page .</p>
  </div>
  <div class="service-card" style="left:757px">
    <div class="head">
      <svg width="44" height="44" viewBox="0 0 44 44" fill="none" stroke="#fff" stroke-width="2"><rect x="4" y="6" width="26" height="30" rx="2"/><path d="M10 16h14M10 22h14M10 28h8"/><circle cx="34" cy="30" r="6"/><path d="M38 34l4 4"/></svg>
      <h3>Information Systems Security Audit</h3>
    </div>
    <p>It is a long established fact that a reader will be distracted by the readable of a page .</p>
  </div>
  <a class="btn" style="left:529px;top:414px;width:142px;height:44px">View All</a>
</section>

<section class="about">
  <svg class="about-bg" width="1200" height="760" viewBox="0 0 1200 760">
    <defs><linearGradient id="aboutGrad" x1="0" y1="0" x2="1" y2="1"><stop offset="0" stop-color="#1b3aa6"/><stop offset="1" stop-color="#132a86"/></linearGradient></defs>
    <path d="M0 0 H1200 V740 C1020 700 900 720 760 760 C600 800 420 740 300 700 C160 650 60 640 0 600 Z" fill="url(#aboutGrad)"/>
    <path d="M0 0 H40 C20 30 6 60 0 90 Z" fill="#ffffff"/>
  </svg>
  <h2>About Us</h2>
  <p class="lead">It is a long established fact that a reader will be distracted by the readable of a page . Many desktop publishing packages and web page editors now .</p>
  <svg class="about-art" viewBox="0 0 435 430" role="img" aria-label="Photo of a hand touching a laptop with a glowing security lock, framed in a shield">
    <defs><linearGradient id="aboutShield" x1="0" y1="0" x2="1" y2="1"><stop offset="0" stop-color="#1d3a70"/><stop offset="0.5" stop-color="#4a5a88"/><stop offset="1" stop-color="#1a2540"/></linearGradient></defs>
    <path d="M218 4 C300 4 380 14 431 38 C431 210 350 350 218 426 C86 350 4 210 4 38 C56 14 136 4 218 4Z" fill="url(#aboutShield)" stroke="#ffffff" stroke-width="4"/>
  </svg>
  <div class="feature" style="top:169px">
    <h4><svg width="33" height="33" viewBox="0 0 33 33"><path d="M16.5 2 L30 7 V15 C30 23 24 29 16.5 31 C9 29 3 23 3 15 V7 Z" fill="#fff"/><path d="M10 16l5 5 8-9" stroke="#1d8fe0" stroke-width="3" fill="none"/></svg>Trusted Partner</h4>
    <p>It is a long established fact that a reader will be distracted by the readable of a page .</p>
  </div>
  <div class="feature" style="top:305px">
    <h4><svg width="33" height="33" viewBox="0 0 33 33"><path d="M16.5 2 L30 7 V15 C30 23 24 29 16.5 31 C9 29 3 23 3 15 V7 Z" fill="#fff"/><circle cx="16.5" cy="16" r="6" fill="none" stroke="#1d8fe0" stroke-width="3"/></svg>System Security</h4>
    <p>It is a long established fact that a reader will be distracted by the readable of a page .</p>
  </div>
  <div class="feature" style="top:441px">
    <h4><svg width="33" height="33" viewBox="0 0 33 33"><path d="M16.5 2 L30 7 V15 C30 23 24 29 16.5 31 C9 29 3 23 3 15 V7 Z" fill="#fff"/><rect x="11" y="14" width="11" height="9" rx="1.5" fill="#1d8fe0"/><path d="M13 14v-3a3.5 3.5 0 0 1 7 0v3" stroke="#1d8fe0" stroke-width="2" fill="none"/></svg>Product Security</h4>
    <p>It is a long established fact that a reader will be distracted by the readable of a page .</p>
  </div>
  <a class="btn" style="left:672px;top:565px;width:142px;height:40px">Read More</a>
</section>

<section class="tech">
  <svg class="tech-bg" width="1200" height="785" viewBox="0 0 1200 785">
    <defs><linearGradient id="techGrad" x1="0" y1="0" x2="1" y2="1"><stop offset="0" stop-color="#1a3aa8"/><stop offset="1" stop-color="#16338f"/></linearGradient></defs>
    <path d="M0 165 C300 120 700 220 1000 330 C1100 370 1160 400 1200 420 V785 H0 Z" fill="url(#techGrad)"/>
  </svg>
  <div class="tech-art" role="img" aria-label="Video still of a hand holding a glowing network lightbulb">
    <div class="play"><svg width="30" height="30" viewBox="0 0 30 30"><circle cx="15" cy="15" r="15" fill="#fff"/><path d="M12 9l9 6-9 6z" fill="#111"/></svg></div>
  </div>
  <h2>Our Technologies</h2>
  <p>Many desktop publishing packages and web page editors now use Lorem Ipsum as their default model text, and a search for 'lorem ipsum' will uncover many web sites still in their infancy. Various versions have evolved over the years, sometimes by accident,</p>
  <a class="btn" style="left:273px;top:649px;width:141px;height:42px">Read More</a>
</section>

<section class="resources">
  <h2 class="section-title">Resources</h2>
  <svg class="abs" style="left:0;top:0" width="1200" height="697" viewBox="0 0 1200 697" fill="none" stroke="#cfd3dd" stroke-width="1.5">
    <path d="M307 208 L345 196 H470"/><circle cx="307" cy="208" r="3" fill="#2aa0ec" stroke="none"/>
    <path d="M922 208 L895 196 H730"/><circle cx="922" cy="208" r="3" fill="#2aa0ec" stroke="none"/>
    <path d="M403 428 L430 414 H540"/><circle cx="403" cy="428" r="3" fill="#2aa0ec" stroke="none"/>
    <path d="M797 428 L770 414 H660"/><circle cx="797" cy="428" r="3" fill="#2aa0ec" stroke="none"/>
  </svg>
  <svg class="res-art" viewBox="0 0 260 255" role="img" aria-label="Illustration of a blue padlock on a silver shield">
    <defs><radialGradient id="resGrad" cx="0.5" cy="0.45" r="0.6"><stop offset="0" stop-color="#2a78d8"/><stop offset="0.55" stop-color="#8fb0dc"/><stop offset="1" stop-color="#e6edf7"/></radialGradient></defs>
    <path d="M130 4 C180 4 225 12 256 28 C256 140 210 215 130 251 C50 215 4 140 4 28 C35 12 80 4 130 4Z" fill="url(#resGrad)"/>
  </svg>
  <div class="res-item" style="left:166px;top:230px"><h4>Lorem Ipsum</h4><p>It is a long established fact that a reader will be distracted by the readable of a page .</p></div>
  <div class="res-item" style="left:774px;top:228px"><h4>Lorem Ipsum</h4><p>It is a long established fact that a reader will be distracted by the readable of a page .</p></div>
  <div class="res-item" style="left:256px;top:452px"><h4>Lorem Ipsum</h4><p>It is a long established fact that a reader will be distracted by the readable of a page .</p></div>
  <div class="res-item" style="left:670px;top:452px"><h4>Lorem Ipsum</h4><p>It is a long established fact that a reader will be distracted by the readable of a page .</p></div>
  <a class="btn" style="left:529px;top:593px;width:142px;height:44px">View All</a>
</section>

<section class="news">
  <h2 class="section-title">Latest News</h2>
  <article class="news-card" style="left:157px">
    <div class="thumb" role="img" aria-label="Photo of a hand touching hexagonal security icons" style="background:linear-gradient(135deg,#2a3a52,#3a5a78 55%,#1b2840)"><div class="date">May 05<br>2021</div></div>
    <h4>Many desktop publishing packages and web page editors.</h4>
    <a class="btn">Read More</a>
  </article>
  <article class="news-card" style="left:458px">
    <div class="thumb" role="img" aria-label="Photo of hands typing on a keyboard with a glowing blue overlay" style="background:linear-gradient(135deg,#1c2a40,#2c5a8a 55%,#11203a)"><div class="date">May 05<br>2021</div></div>
    <h4>Many desktop publishing packages and web page editors.</h4>
    <a class="btn">Read More</a>
  </article>
  <article class="news-card" style="left:757px">
    <div class="thumb" role="img" aria-label="Photo of a hand holding a glowing blue shield" style="background:linear-gradient(135deg,#0f2a78,#2d6ae0 55%,#0c1b50)"><div class="date">May 05<br>2021</div></div>
    <h4>Many desktop publishing packages and web page editors.</h4>
    <a class="btn">Read More</a>
  </article>
</section>

<section class="partners">
  <h2 class="section-title">Our Partners</h2>
  <div class="partner" style="left:180px"><i></i>Pubrix</div>
  <div class="partner" style="left:385px"><i></i>Solvanta</div>
  <div class="partner" style="left:560px"><i></i>Brandel</div>
  <div class="partner" style="left:725px"><i></i>Logora</div>
  <div class="partner" style="left:890px"><i></i>Comvari</div>
  <div class="dots" style="left:575px;top:270px;color:#8a8a96"><span class="ring"></span><span style="background:#1b2a7c"></span><span class="ring"></span></div>
</section>

<footer class="site-footer">
  <div class="brand"><span class="brand-dot"></span>Vantrel Works</div>
  <p class="footer-about">Many desktop publishing packages and web page editors now use Lorem Ipsum as their default model text,</p>
  <div class="contact-line" style="top:268px">
    <svg width="12" height="16" viewBox="0 0 12 16"><path d="M6 0a6 6 0 0 1 6 6c0 4-6 10-6 10S0 10 0 6a6 6 0 0 1 6-6z" fill="#2aa0ec"/><circle cx="6" cy="6" r="2" fill="#16297c"/></svg>
    <span>418 Harlow Street<br>Brennick Falls, USA</span>
  </div>
  <div class="contact-line" style="top:326px">
    <svg width="12" height="14" viewBox="0 0 14 14"><path d="M3 0l3 3-2 2c1 2 3 4 5 5l2-2 3 3-2 3C6 14 0 8 0 2z" fill="#2aa0ec"/></svg>
    <span>Phone: 555-014-2290</span>
  </div>
  <div class="contact-line" style="top:366px">
    <svg width="13" height="13" viewBox="0 0 14 14" fill="none" stroke="#2aa0ec" stroke-width="1.5"><circle cx="7" cy="7" r="6"/><path d="M7 3v4h3"/></svg>
    <span>Mon-Fri: 8:00 a.m. – 5:00 p.m.</span>
  </div>
  <div class="footer-col" style="left:514px">
    <h5>OUR SERVICES</h5>
    <ul><li>Consulting</li><li>Vulnerability<br>assessment</li><li>Information<br>systems<br>security audit</li><li>ISO compliance</li><li style="margin-top:22px">Penetration testing</li></ul>
  </div>
  <div class="footer-col" style="left:733px">
    <h5>QUICK LINK</h5>
    <ul><li>Home</li><li>Services</li><li>About us</li><li>Resources</li><li>Technologies</li><li>Careers</li><li>Partners</li><li>Blog</li><li>Contacts</li></ul>
  </div>
  <div class="footer-col" style="left:904px">
    <h5>RESOURCES</h5>
    <ul><li>Lorem Ipsum</li><li>Lorem Ipsum</li><li>Lorem Ipsum</li><li>Lorem Ipsum</li></ul>
  </div>
  <p class="copyright">Copyright©2021 vantrelworks , All Rights Reserved.</p>
  <div class="follow">Follow Us : <span class="s"></span><span class="s"></span><span class="s"></span></div>
</footer>

</div>
</body>
</html>
```